Copy and paste the text for the first 3 pages of the changes sheet – please follow the instructions on the other pages
Copy all of the items from the menu and make the changes below:
1. Add under Signature Dish
a. Asian Sizzling Salmon $16.95
Wok seared Alaska salmon served with a sweet sesame garlic glaze on a bed of asparagus.
b. Mongolian Beef $17.95
Wok’d filet mignon with sliced red and green onions in a garlic ginger soy sauce.
2. Add under Appetizers
a. Po Vi Nar Nachos $9.95
Seasoned Won Ton chips covered with cheddar Jack cheese, tomatoes, red and green onions, jalapenos, and bacon bits. Served with wasabi sour cream, guacamole and a sweet and spicy dipping sauce.
b. Dang Dang Chicken $5.95
Tender chunks of marinated chicken lightly fried with a coconut batter and drizzled with a special sauce.
c. Korean Beef Tacos $8.95
Two Tacos filled with w/marinated flank steak, kim chee, sliced onions on a corn tortilla
d. Duck Quesadilla $9.99
Tender shredded duck breast sandwiched between scallion pancakes and asian hoisin sauce.
3. Add under American Fare
a. Po Vi Nar Burger $9.95
Our 8oz burgers are made from fresh Angus chunk, ground in our kitchen and served on a toasted artisan roll and topped with lettuce, tomato and red onion. Served with French fries and coleslaw. Add Cheese - .50

```html
<!DOCTYPE html>
<html lang="en">
<head>
<meta charset="utf-8">
<title>Po Vi Nar Menu</title>
<link href="https://fonts.googleapis.com/css2?family=Roboto+Slab:wght@700;800&family=Courier+Prime:wght@400;700&display=swap" rel="stylesheet">
<style>
:root{
  --page:#ecebe7;
  --paper:#f4f0e4;
  --red:#b3282c;
  --green:#3e8a3b;
  --ink:#2b2622;
  --soft:#5a524a;
  --floral-a:#f4f0e4;
  --floral-b:#e2dccb;
}
*{margin:0;padding:0;box-sizing:border-box}
html,body{width:1200px;height:898px;overflow:hidden;background:var(--page)}
body{position:relative;font-family:"Courier Prime",monospace;color:var(--ink)}
.panel{position:absolute;top:8px;width:388px;height:882px;background:var(--paper);overflow:hidden;padding:8px 16px 0}
.panel--left{left:8px}.panel--mid{left:404px}.panel--right{left:800px}
.floral{position:absolute;left:0;right:0;bottom:0;height:300px;background:linear-gradient(180deg,var(--floral-a),var(--floral-b));z-index:0}
.content{position:relative;z-index:1}
.brand{display:flex;flex-direction:column;align-items:center;gap:2px;margin-bottom:4px}
.brand-dot{width:12px;height:12px;border-radius:50%;background:var(--green)}
.brand-name{font-family:"Roboto Slab",serif;font-weight:700;font-size:7px;color:var(--green);letter-spacing:1px}
.bar{border-top:1px solid var(--red);border-bottom:1px solid var(--red);text-align:center;font-family:"Roboto Slab",serif;font-weight:800;color:var(--green);font-size:14px;letter-spacing:1px;padding:2px 0;margin:4px 0}
.bar--top{font-size:15px}
.title-red{text-align:center;font-family:"Roboto Slab",serif;font-weight:800;color:var(--red);font-size:12px;margin:2px 0}
.title-green{text-align:center;font-family:"Roboto Slab",serif;font-weight:800;color:var(--green);font-size:17px;margin:2px 0}
.note{font-size:5.5px;line-height:1.35;text-align:center;color:var(--soft);margin:2px 6px}
.cols{display:flex;gap:14px;margin:4px 0}
.cols>ul{flex:1;list-style:none}
.price-list li{display:flex;justify-content:space-between;font-size:8.5px;line-height:1.28}
.feature{text-align:center;margin:3px 0}
.feature .name{font-size:7.5px;font-weight:700}
.feature .desc{font-size:5.5px;line-height:1.3;color:var(--soft)}
.sig{text-align:center;margin-bottom:7px}
.sig .name{font-size:8.5px;font-weight:700}
.sig .desc{font-size:5.3px;line-height:1.3;color:var(--soft)}
.sig .price{font-size:8px;font-weight:700}
.fare li{display:flex;justify-content:space-between;font-size:10px;line-height:1.3;font-weight:700}
.combo-grid{display:grid;grid-template-columns:repeat(3,1fr);gap:6px 8px;margin-top:4px}
.combo{text-align:center}
.combo .name{font-size:7.5px;font-weight:700}
.combo .desc{font-size:4.8px;line-height:1.3;color:var(--soft)}
.combo .price{font-size:6.5px;font-weight:700}
.dessert{text-align:center;margin:6px 0}
.dessert .name{font-size:9px;font-weight:700}
.dessert .desc{font-size:5.3px;color:var(--soft)}
.dessert .price{font-size:8px;font-weight:700}
.fine{font-size:4.8px;line-height:1.35;color:var(--soft);text-align:center;margin-top:10px}
</style>
</head>
<body>

<section class="panel panel--left">
  <div class="floral" role="img" aria-label="Faint tropical floral pattern along the bottom of the panel"></div>
  <div class="content">
    <div class="brand"><span class="brand-dot"></span><span class="brand-name">PO VI NAR</span></div>
    <div class="title-red">TRY OUR FAMOUS PU PU PLATTER</div>
    <p class="note">An island sampler served for two or more with fried shrimp, BBQ chicken wings, crab rangoon, gold fingers, teriyaki beef, egg rolls and BBQ boneless ribs, warmed at your table over a flaming hibachi. $14.95 per person.</p>
    <div class="bar">APPETIZERS</div>
    <div class="cols">
      <ul class="price-list">
        <li><span>Fried Shrimp</span><span>$ 9.95</span></li>
        <li><span>BBQ Chicken Wings</span><span>$ 5.95</span></li>
        <li><span>Crab Rangoon</span><span>$ 5.95</span></li>
        <li><span>Gold Fingers</span><span>$ 7.95</span></li>
        <li><span>Teriyaki Beef</span><span>$ 7.95</span></li>
        <li><span>Egg Rolls (4)</span><span>$ 5.95</span></li>
        <li><span>Egg Rolls (1)</span><span>$ 2.50</span></li>
        <li><span>Ravioli Rolls (4)</span><span>$ 5.95</span></li>
        <li><span>BBQ Boneless Ribs</span><span>$ 9.95</span></li>
        <li><span>BBQ Spare Ribs w/ Bone*</span><span>$ 9.95</span></li>
      </ul>
      <ul class="price-list">
        <li><span>Pot Stickers</span><span>$ 6.95</span></li>
        <li><span>Vegetable Tempura</span><span>$ 6.95</span></li>
        <li><span>Fried Pineapple</span><span>$ 7.95</span></li>
        <li><span>Teriyaki Chicken</span><span>$ 6.95</span></li>
        <li><span>Coconut Shrimp</span><span>$ 9.95</span></li>
        <li><span>Salt &amp; Pepper Calamari</span><span>$ 9.95</span></li>
        <li><span>Rumaki</span><span>$ 6.95</span></li>
        <li><span>French Fries</span><span>$ 2.95</span></li>
        <li><span>Garlic Bites*</span><span>$ 4.95</span></li>
      </ul>
    </div>
    <div class="feature"><div class="name">Tikigai Wings $9.95</div><div class="desc">Crispy wings tossed in a sweet chili glaze with toasted sesame and scallions.</div></div>
    <div class="feature"><div class="name">Salt &amp; Pepper Wings $7.95</div><div class="desc">Wings wok tossed with garlic, peppers and sea salt.</div></div>
    <div class="feature"><div class="name">Chicken Lettuce Wraps $9.99</div><div class="desc">Minced chicken, water chestnuts and mushrooms served with cool lettuce cups.</div></div>
    <div class="feature"><div class="name">Po Vi Nar Nachos $9.95</div><div class="desc">Seasoned Won Ton chips covered with cheddar Jack cheese, tomatoes, red and green onions, jalapenos, and bacon bits. Served with wasabi sour cream, guacamole and a sweet and spicy dipping sauce.</div></div>
    <div class="feature"><div class="name">Dang Dang Chicken $5.95</div><div class="desc">Tender chunks of marinated chicken lightly fried with a coconut batter and drizzled with a special sauce.</div></div>
    <div class="feature"><div class="name">Korean Beef Tacos $8.95</div><div class="desc">Two Tacos filled with w/marinated flank steak, kim chee, sliced onions on a corn tortilla</div></div>
    <div class="feature"><div class="name">Duck Quesadilla $9.99</div><div class="desc">Tender shredded duck breast sandwiched between scallion pancakes and asian hoisin sauce.</div></div>
    <div class="bar">SOUPS</div>
    <div class="cols">
      <ul class="price-list">
        <li><span>Traditional Won Ton Soup</span><span>$ 3.75</span></li>
        <li><span>Egg Drop Soup</span><span>$ 3.50</span></li>
        <li><span>Hot &amp; Sour Soup</span><span>$ 3.75</span></li>
      </ul>
      <ul class="price-list">
        <li><span>Chicken Rice or Noodle</span><span>$ 3.99</span></li>
        <li><span>Seafood Tofu Soup</span><span>$ 3.99</span></li>
        <li><span>Chicken Corn Soup</span><span>$ 3.99</span></li>
      </ul>
    </div>
    <div class="feature"><div class="name">Island Seafood Soup $9.99</div><div class="desc">Shrimp, scallops and crab in a light broth with greens, served for two.</div></div>
    <div class="bar">SALADS</div>
    <div class="feature"><div class="name">Ahi Tuna Salad $11.95</div><div class="desc">Seared ahi over mixed greens with ginger sesame dressing.</div></div>
    <div class="feature"><div class="name">Thai Chicken Salad $8.95</div><div class="desc">Grilled chicken, crisp noodles, cabbage and peanut lime dressing.</div></div>
    <div class="feature"><div class="name">Garden Salad $4.95</div></div>
  </div>
</section>

<section class="panel panel--mid">
  <div class="floral" role="img" aria-label="Faint tropical floral pattern along the bottom of the panel"></div>
  <div class="content">
    <div class="bar bar--top">WELCOME TO THE PO VI NAR</div>
    <p class="note">For over forty years our family has welcomed guests to share the flavors of the islands. Every dish is prepared fresh to order in our kitchen using traditional recipes and the finest ingredients. Sit back, enjoy a tropical drink and let us take care of the rest.</p>
    <p class="note">Please let your server know of any allergies or dietary needs before ordering.</p>
    <div class="title-green">SIGNATURE DISHES</div>
    <p class="note">Chef's favorites served with steamed or fried rice and a cup of soup.</p>
    <div class="cols">
      <div style="flex:1">
        <div class="sig"><div class="name">Pan-Seared Ahi Tuna</div><div class="desc">Sesame crusted ahi seared rare with wasabi glaze and stir fried greens.</div><div class="price">$18.95</div></div>
        <div class="sig"><div class="name">Lobster Fried Rice</div><div class="desc">Maine lobster tossed with egg, peas and scallions in a hot wok.</div><div class="price">Market Price</div></div>
        <div class="sig"><div class="name">Seafood Gourmet</div><div class="desc">Shrimp, scallops and crab with fresh vegetables in white wine sauce.</div><div class="price">$17.95</div></div>
        <div class="sig"><div class="name">Beef Tenderloin with Pea Pods</div><div class="desc">Sliced tenderloin with crisp pea pods in a rich oyster sauce.</div><div class="price">$16.95</div></div>
        <div class="sig"><div class="name">Fire Grilled Chicken Teriyaki</div><div class="desc">Marinated chicken breast grilled and brushed with house teriyaki.</div><div class="price">$13.95</div></div>
        <div class="sig"><div class="name">Dan Dan Noodles</div><div class="desc">Fresh noodles with spiced pork, chili oil and crushed peanuts.</div><div class="price">$11.95</div></div>
        <div class="sig"><div class="name">Sweet Martinis</div><div class="desc">Crispy shrimp in a creamy honey glaze with candied walnuts.</div><div class="price">$15.95</div></div>
        <div class="sig"><div class="name">Walking Pork Chops</div><div class="desc">Salt and pepper pork chops with garlic and sliced peppers.</div><div class="price">$14.95</div></div>
        <div class="sig"><div class="name">Polynesian Delight</div><div class="desc">Chicken, shrimp and pineapple in a sweet island sauce.</div><div class="price">$15.95</div></div>
        <div class="sig"><div class="name">Triple Delight</div><div class="desc">Beef, chicken and shrimp with mixed vegetables in brown sauce.</div><div class="price">$16.95</div></div>
      </div>
      <div style="flex:1">
        <div class="sig"><div class="name">Asian Sizzling Salmon</div><div class="desc">Wok seared Alaska salmon served with a sweet sesame garlic glaze on a bed of asparagus.</div><div class="price">$16.95</div></div>
        <div class="sig"><div class="name">Chicken Bao Bao</div><div class="desc">Tender chicken with cashews and vegetables in a spicy glaze.</div><div class="price">$12.95</div></div>
        <div class="sig"><div class="name">Mongolian Beef</div><div class="desc">Wok'd filet mignon with sliced red and green onions in a garlic ginger soy sauce.</div><div class="price">$17.95</div></div>
        <div class="sig"><div class="name">Japanese Steak</div><div class="desc">Grilled strip steak sliced over onions with ginger sauce.</div><div class="price">$18.95</div></div>
        <div class="sig"><div class="name">Crispy Orange Duck</div><div class="desc">Half duck roasted crisp with a bright orange glaze.</div><div class="price">$17.95</div></div>
        <div class="sig"><div class="name">Twin Lobster Stir-fry</div><div class="desc">Two lobster tails wok tossed with ginger and scallions.</div><div class="price">Market Price</div></div>
        <div class="sig"><div class="name">General's Chicken</div><div class="desc">Crispy chicken in a sweet and spicy chili sauce.</div><div class="price">$12.95</div></div>
        <div class="sig"><div class="name">Po Vi Nar Cantonese Noodle</div><div class="desc">Pan fried noodles topped with shrimp, chicken, pork and greens.</div><div class="price">$14.95</div></div>
        <div class="sig"><div class="name">Happy Family</div><div class="desc">Lobster, shrimp, beef and chicken with vegetables.</div><div class="price">$18.95</div></div>
      </div>
    </div>
  </div>
</section>

<section class="panel panel--right">
  <div class="floral" role="img" aria-label="Faint tropical floral pattern along the bottom of the panel"></div>
  <div class="content">
    <div class="title-green" style="font-size:18px;margin-top:2px">AMERICAN FARE</div>
    <p class="note">Served with French fries and coleslaw</p>
    <ul class="fare" style="list-style:none;margin:6px 14px">
      <li><span>16 oz. New York Sirloin*</span><span>$19.99</span></li>
      <li><span>Fried Scallops</span><span>$15.99</span></li>
      <li><span>Fish &amp; Chips</span><span>$13.99</span></li>
      <li><span>Broiled Maine Lobster</span><span>Market Price</span></li>
      <li><span>Po Vi Nar Burger</span><span>$9.95</span></li>
    </ul>
    <p class="note">Our 8oz burgers are made from fresh Angus chunk, ground in our kitchen and served on a toasted artisan roll and topped with lettuce, tomato and red onion. Served with French fries and coleslaw. Add Cheese - .50</p>
    <div class="bar" style="font-size:15px">DINNER COMBINATIONS</div>
    <p class="note">All dinners include egg roll, soup of the day and steamed or fried rice. No substitutions please.</p>
    <div class="combo-grid">
      <div class="combo"><div class="name">DINNER A</div><div class="desc">Chicken Chop Suey, Egg Roll, Fried Rice</div><div class="price">$10.95</div></div>
      <div class="combo"><div class="name">DINNER B</div><div class="desc">Sweet &amp; Sour Pork, Egg Roll, Fried Rice</div><div class="price">$11.95</div></div>
      <div class="combo"><div class="name">DINNER C</div><div class="desc">Beef Broccoli, Crab Rangoon, Fried Rice</div><div class="price">$12.95</div></div>
      <div class="combo"><div class="name">DINNER D</div><div class="desc">Moo Goo Gai Pan, Egg Roll, Fried Rice</div><div class="price">$11.95</div></div>
      <div class="combo"><div class="name">DINNER E</div><div class="desc">Shrimp Lo Mein, Pot Stickers, Fried Rice</div><div class="price">$12.95</div></div>
      <div class="combo"><div class="name">DINNER F</div><div class="desc">Cashew Chicken, Egg Roll, Fried Rice</div><div class="price">$11.95</div></div>
      <div class="combo"><div class="name">DINNER G</div><div class="desc">Pepper Steak, Gold Fingers, Fried Rice</div><div class="price">$12.95</div></div>
      <div class="combo"><div class="name">DINNER H</div><div class="desc">Kung Pao Chicken, Egg Roll, Fried Rice</div><div class="price">$11.95</div></div>
      <div class="combo"><div class="name">DINNER I</div><div class="desc">Shrimp Chow Mein, Rangoon, Fried Rice</div><div class="price">$12.95</div></div>
      <div class="combo"><div class="name">DINNER J</div><div class="desc">Orange Chicken, Egg Roll, Fried Rice</div><div class="price">$11.95</div></div>
      <div class="combo"><div class="name">DINNER K</div><div class="desc">Mongolian Beef, Egg Roll, Fried Rice</div><div class="price">$13.95</div></div>
      <div class="combo"><div class="name">DINNER L</div><div class="desc">Garlic Shrimp, Pot Stickers, Fried Rice</div><div class="price">$13.95</div></div>
      <div class="combo"><div class="name">DINNER M</div><div class="desc">Lemon Chicken, Egg Roll, Fried Rice</div><div class="price">$11.95</div></div>
      <div class="combo"><div class="name">DINNER O</div><div class="desc">Vegetable Delight, Egg Roll, Fried Rice</div><div class="price">$10.95</div></div>
    </div>
    <div class="bar" style="font-size:15px;margin-top:10px">DESSERT</div>
    <div class="dessert"><div class="name">Tempura Fried Cheese Cake</div><div class="desc">Creamy cheesecake in a light batter with berry sauce.</div><div class="price">$5.99</div></div>
    <div class="dessert"><div class="name">Fried Banana</div><div class="desc">Golden banana with honey and sesame.</div><div class="price">$4.99</div></div>
    <div class="dessert"><div class="name">Molten Lava Explosion Cake</div><div class="desc">Warm chocolate cake with a melting center.</div><div class="price">$6.99</div></div>
    <div class="dessert"><div class="name">Vanilla Ice Cream</div><div class="price">$2.99</div></div>
    <p class="fine">*Consuming raw or undercooked meats, poultry, seafood or eggs may increase your risk of foodborne illness. A gratuity may be added to parties of six or more. Prices subject to change.</p>
  </div>
</section>

</body>
</html>
```